Geschäftspapier-Design für Anbieter einer Online-Ausbildung für den qualifizierten Krankentransport und Rettungsdienst
Zielgruppe
VOLT Online-Ausbildung für den qualifizierten Krankentransport und Rettungsdienst
Der qualifizierte Krankentransport und Rettungsdienst ist zuständig für den Transport- und die Versorgung von kranken und verletzten Menschen. VOLT Medizinische Ausbildung und Seminare hat sich als Privatschule für die präklinische Notfallmedizin auf Aus- und Weiterbildungen im E-Learning-Modul für diese zwei Fachbereiche spezialisiert. Alle unsere Fachausbildungen sind online in unserem modernen Campus mit überregionalem Zugang absolvierbar.
Aufgabenstellung
Wir benötigen eine Word-Briefvorlage für den alltäglichen Geschäftsverkehr in drei Ausführungen.
- Briefvorlage mit Angabe der Abteilung -> Sekretariat
- Briefvorlage mit Angabe der Abteilung -> Schulleitung
- Briefvorlage mit Angabe der Abteilung -> Geschäftsführung
- Briefvorlage mit Angabe der Abteilung -> Buchhaltung/ Forderungsmanagement
Die Vorlage sollte bitte folgende Angaben aufweisen:
VOLT Bildungsgesellschaft UG (haftungsbeschränkt)
Privatschule für prähospitale Rettungsmedizin
Standort unserer Verwaltung:
Distelgrund 7
15299 Waldmoor
Standort unseres Schulsitzes:
Am Wiesenhang 41
D- 15537 Gosen- Neu Zittau
Schulleitung: Petra Hollmann & Matthias Wol
Ärztliche Leitung: Dr. Med. Jörg Paulsen
Pädagogische Leitung: Matthias Volt
Fachlicher Beirat: Dr. rer. med. Florian Ostrowski
Tel: 030 6273804 52
Fax: 030 6273804 53
E-Mail: info@volt-lehrwerkstatt-beispiel.de
Web: www.volt-lehrwerkstatt-beispiel.de
Vertreten durch: Petra Hollmann
Registereintrag: Eintragung im Handelsregister Registergericht: Amtsgericht Seefeld Registernummer: HRB 24830 FF

```html
<!DOCTYPE html>
<html lang="de">
<head>
<meta charset="utf-8">
<title>VOLT Briefvorlage – Sekretariat</title>
<link rel="stylesheet" href="https://fonts.googleapis.com/css2?family=Open+Sans:wght@400;600;700;800&display=swap">
<style>
  :root {
    --blue: #6ba7da;
    --blue-dark: #4f7fa8;
    --ink: #1f1f21;
    --grey: #8a8a8a;
    --paper: #ffffff;
  }
  * { margin: 0; padding: 0; box-sizing: border-box; }
  html, body { width: 848px; height: 1200px; overflow: hidden; background: var(--paper); }
  body { font-family: "Open Sans", Arial, sans-serif; color: var(--ink); position: relative; }

  .header-shapes { position: absolute; left: 0; top: 0; width: 848px; height: 220px; }
  .department {
    position: absolute; left: 620px; top: 1px;
    font-size: 17px; font-weight: 700; letter-spacing: 4px; color: var(--blue);
  }

  .brand { position: absolute; left: 580px; top: 104px; width: 170px; text-align: right; }
  .brand-name { font-size: 52px; font-weight: 800; line-height: 56px; letter-spacing: 3px; color: var(--ink); display: flex; align-items: center; justify-content: flex-end; gap: 8px; }
  .brand-mark { width: 34px; height: 34px; background: var(--blue); display: inline-block; }
  .brand-tagline { font-size: 8px; font-weight: 700; color: var(--ink); margin-top: 1px; white-space: nowrap; }

  .recipient { position: absolute; left: 100px; top: 243px; }
  .recipient-name { font-size: 19px; font-weight: 700; }
  .recipient-address { margin-top: 15px; font-size: 13px; line-height: 18.5px; color: var(--grey); }
  .letter-date { position: absolute; right: 98px; top: 331px; font-size: 13px; color: var(--ink); }

  .letter-body { position: absolute; left: 100px; top: 388px; width: 650px; }
  .letter-body p { font-size: 12.8px; line-height: 18.3px; color: var(--grey); text-align: justify; margin-bottom: 18.3px; }

  .signature-mark { position: absolute; left: 118px; top: 831px; width: 204px; height: 70px; background: linear-gradient(90deg, rgba(107,167,218,0.25), rgba(107,167,218,0.45)); border-radius: 4px; }
  .signer { position: absolute; left: 152px; top: 899px; }
  .signer-name { font-size: 19px; font-weight: 700; }
  .signer-role { font-size: 13px; color: var(--grey); margin-top: 1px; }

  .footer-mark { position: absolute; left: 97px; top: 1077px; width: 47px; height: 52px; background: var(--blue); }
  .footer-tagline { position: absolute; left: 172px; top: 1073px; font-size: 14.6px; color: var(--blue); white-space: nowrap; }
  .contact { position: absolute; top: 1101px; display: flex; align-items: center; gap: 11px; font-size: 12.3px; line-height: 14.5px; color: var(--ink); white-space: nowrap; }
  .contact svg { width: 24px; height: 24px; flex: none; }
  .contact-phone { left: 169px; }
  .contact-address { left: 348px; }
  .contact-web { left: 520px; }

  .footer-band { position: absolute; left: 0; top: 1167px; width: 848px; height: 33px; }
  .register { position: absolute; right: 92px; top: 1169px; font-size: 11.6px; line-height: 14px; text-align: right; color: var(--ink); white-space: nowrap; }
</style>
</head>
<body>

<svg class="header-shapes" viewBox="0 0 848 220" aria-hidden="true">
  <polygon points="0,0 497,0 484,25 173,25 0,217" fill="var(--blue)"/>
  <polygon points="0,0 49,0 49,52 0,99" fill="var(--paper)"/>
  <polygon points="112,0 170,0 0,188 0,125" fill="var(--paper)"/>
  <polygon points="508,0 848,0 848,25 492,25" fill="var(--ink)"/>
</svg>
<div class="department">Sekretariat</div>

<div class="brand">
  <div class="brand-name"><span class="brand-mark"></span>VOLT</div>
  <div class="brand-tagline">Medizinische Ausbildung u. Seminare</div>
</div>

<div class="recipient">
  <div class="recipient-name">Matthias Wol</div>
  <div class="recipient-address">
    Distelgrund 7<br>
    15299 Waldmoor · kontakt@beispielpost.de<br>
    030 6273804 52
  </div>
</div>
<div class="letter-date">Date, 10 october, 2022</div>

<div class="letter-body">
  <p>Lorem ipsum dolor sit amet, consectetur adipisicing elit, sed do eiusmod tempor incididunt ut labore et dolore magna aliqua. Ut enim ad minim veniam, quis nostrud exercitation ullamco laboris nisi ut aliquip ex ea commodo consequat. Duis aute irure dolor in reprehenderit in voluptate velit esse cillum dolore eu fugiat nulla pariatur. Excepteur sint occaecat cupidatat non proident, sunt in culpa qui officia deserunt mollit anim id est laborum. Sed ut perspiciatis unde omnis iste natus error sit voluptatem accusantium doloremque laudantium, totam rem aperiam, eaque ipsa quae ab illo inventore veritatis et quasi architecto beatae vitae dicta sunt explicabo. Nemo enim ipsam voluptatem quia voluptas sit aspernatur aut odit aut fugit, sed quia consequuntur magni dolores eos qui ratione voluptatem sequi nesciunt. Neque porro voluptatem sequi nesciunt. Nemo enim ipsam voluptatem quia voluptas.</p>
  <p>Lorem ipsum dolor sit amet, consectetur adipisicing elit, sed do eiusmod tempor incididunt ut labore et dolore magna aliqua. Ut enim ad minim veniam, quis nostrud exercitation ullamco laboris nisi ut aliquip ex ea commodo consequat. Duis aute irure dolor in reprehenderit in voluptate velit esse cillum dolore eu fugiat nulla pariatur. Excepteur sint occaecat cupidatat non proident, sunt in culpa qui officia deserunt mollit anim id est laborum. Sed ut perspiciatis unde omnis iste natus error sit voluptatem accusantium doloremque laudantium, totam rem aperiam, eaque ipsa quae ab illo inventore veritatis et quasi architecto beatae vitae dicta sunt explicabo. Nemo enim ipsam voluptatem quia voluptas sit aspernatur aut odit aut.</p>
  <p>Lorem ipsum dolor sit amet, consectetur adipisicing elit, sed do eiusmod tempor incididunt ut labore et dolore magna aliqua. Ut enim ad minim veniam, quis nostrud exercitation ullamco laboris nisi ut aliquip ex ea commodo consequat. .</p>
</div>

<div class="signature-mark" role="img" aria-label="Handschriftliche Unterschrift von Petra Hollmann"></div>
<div class="signer">
  <div class="signer-name">Petra Hollmann</div>
  <div class="signer-role">General Manager</div>
</div>

<div class="footer-mark"></div>
<div class="footer-tagline">VOLT Online-Ausbildung für den qualifizierten Krankentransport und Rettungsdienst</div>

<div class="contact contact-phone">
  <svg viewBox="0 0 24 24" aria-hidden="true">
    <rect width="24" height="24" fill="var(--blue)"/>
    <polygon points="0,24 24,0 24,24" fill="var(--blue-dark)"/>
    <path d="M6 10c0-2 3-3 6-3s6 1 6 3v1h-3v-1.5h-6V11H6z M8 12h8l1 5H7z" fill="#fff"/>
  </svg>
  <div>030 6273804 52<br>030 6273804 53</div>
</div>
<div class="contact contact-address">
  <svg viewBox="0 0 24 24" aria-hidden="true">
    <rect width="24" height="24" fill="var(--blue)"/>
    <polygon points="0,24 24,0 24,24" fill="var(--blue-dark)"/>
    <path d="M12 5a4.5 4.5 0 0 0-4.5 4.5C7.5 13 12 18 12 18s4.5-5 4.5-8.5A4.5 4.5 0 0 0 12 5z" fill="#fff"/>
    <circle cx="12" cy="9.5" r="1.6" fill="var(--blue)"/>
  </svg>
  <div>Distelgrund 7<br>15299 Waldmoor</div>
</div>
<div class="contact contact-web">
  <svg viewBox="0 0 24 24" aria-hidden="true">
    <rect width="24" height="24" fill="var(--blue)"/>
    <polygon points="0,24 24,0 24,24" fill="var(--blue-dark)"/>
    <circle cx="12" cy="12" r="6" fill="none" stroke="#fff" stroke-width="1.4"/>
    <path d="M6 12h12M12 6c-2.5 3-2.5 9 0 12M12 6c2.5 3 2.5 9 0 12" fill="none" stroke="#fff" stroke-width="1.1"/>
  </svg>
  <div>info@volt-lehrwerkstatt-beispiel.de<br>www.volt-lehrwerkstatt-beispiel.de</div>
</div>

<svg class="footer-band" viewBox="0 0 848 33" aria-hidden="true">
  <polygon points="0,0 327,0 298,33 0,33" fill="var(--ink)"/>
  <polygon points="336,0 848,0 848,33 307,33" fill="var(--blue)"/>
</svg>
<div class="register">
  Eintragung im Handelsregister<br>
  Registergericht: Amtsgericht Seefeld Registernummer: HRB 24830 FF
</div>

</body>
</html>
```